Love-Drama Movie Flyer for World Sales Pitch

Dear Designers

We need for a world sales pitch a flyer for our new movie MARBLEFIN. We need a front and a back page A4.
Front: One picture we deliver for then whole page, title, some "pitch" sentences
Picture Front: https://www.fileharbor-example.net/s/qk83tnb2px71vd9/Front_Picture.jpg?dl=0
Back: Arrangement of title, 5 pictures and text we deliver (attached)

Please find in the attached examples a rough idea what we’re looking for. Should not be exactly the same.

To get an Impression of the content and style of the film, please watch the 3min teaser. This will be very important for the style of the flyer:
https://clipvault-example.net/487316920
pw: tutumarblefin

In the end we prefer a data package with the flyer made in a adobe design application for high quality print.

Thanks
Tomas Vrelnik
Producer

Target Market(s)

High profile film sales professionals

Industry/Entity Type

Film Production

Requirements
Must have
• see description
Should not have
• not too generic,
• there is the color red on the actors pullover but red is not really a color in the film. So please don't use much red
• Awards of the actor/actress are not for this movie, it's from other movies

```html
<!DOCTYPE html>
<html lang="en">
<head>
<meta charset="utf-8">
<title>MARBLEFIN – Flyer Back</title>
<link rel="stylesheet" href="https://fonts.googleapis.com/css2?family=Roboto:ital,wght@0,100;0,300;0,400;0,700;1,300&display=swap">
<style>
  :root {
    --page-bg: #ffffff;
    --teal-deep: #0d3340;
    --teal-mid: #2f7283;
    --teal-light: #6fb2bd;
    --ink-black: #111114;
    --ink-quote: #1c2b30;
    --text-light: #d6d6d6;
    --text-white: #ffffff;
    --accent-red: #d2261d;
    --note-grey: #8a8a8a;
  }
  * { margin: 0; padding: 0; box-sizing: border-box; }
  html, body { width: 1200px; height: 1000px; overflow: hidden; background: var(--page-bg); }
  body { font-family: "Roboto", Arial, sans-serif; position: relative; }

  .flyer {
    position: absolute; left: 82px; top: 0; width: 707px; height: 1000px;
    background: var(--ink-black); overflow: hidden;
  }
  .hero-photo {
    position: absolute; left: 0; top: 0; width: 707px; height: 386px;
    background: radial-gradient(ellipse at 45% 20%, var(--teal-light) 0%, var(--teal-mid) 40%, var(--teal-deep) 100%);
  }
  .hero-quote {
    position: absolute; left: 460px; top: 100px; width: 210px;
    font-style: italic; font-weight: 300; font-size: 15px; line-height: 23.5px;
    color: var(--ink-quote); text-align: right;
  }
  .hero-quote .red { color: var(--accent-red); }
  .qmark { font-weight: 700; font-style: normal; font-size: 24px; color: var(--ink-quote); line-height: 0; }
  .title {
    position: absolute; left: 0; width: 707px; top: 308px; text-align: center;
    font-weight: 300; font-size: 78px; letter-spacing: 1px; color: #cfcfcf; line-height: 1;
  }
  .still-strip { position: absolute; left: 0; top: 390px; width: 707px; height: 94px; display: flex; gap: 2px; }
  .still { flex: 1; }
  .still.gym { background: linear-gradient(135deg, #7d8c8a, #3f4a4b); }
  .still.portrait { background: linear-gradient(135deg, #4a3a33, #1f1a18); }
  .still.pregnant { background: linear-gradient(135deg, #5a5650, #2a2826); }
  .still.father { background: linear-gradient(135deg, #6e7474, #2d3232); }

  .figure-shadow {
    position: absolute; left: 430px; top: 484px; width: 277px; height: 516px;
    background: radial-gradient(ellipse at 55% 30%, #2c2c30 0%, #18181b 55%, var(--ink-black) 100%);
  }
  .synopsis {
    position: absolute; left: 63px; top: 532px; width: 380px;
    color: var(--text-light); font-size: 15px; line-height: 20.3px; text-align: justify; font-weight: 300;
  }
  .synopsis .lead { font-size: 21px; }
  .synopsis b { font-weight: 400; font-size: 18px; color: var(--text-white); }
  .synopsis .qmark { color: var(--text-light); font-size: 22px; }
  .syn-open { position: absolute; left: 42px; top: 532px; color: var(--text-light); font-weight: 700; font-size: 22px; }
  .specs {
    position: absolute; left: 63px; top: 766px; color: var(--text-light);
    font-weight: 700; font-size: 13px; line-height: 20px;
  }
  .specs .red { color: var(--accent-red); }
  .contact { position: absolute; left: 63px; top: 858px; color: var(--text-light); font-size: 12.5px; line-height: 17px; font-weight: 300; }
  .contact h3 {
    font-weight: 300; font-size: 19px; color: var(--accent-red); line-height: 20px;
    display: inline-block; border-bottom: 1px solid var(--accent-red); padding-right: 4px; margin-bottom: 6px;
  }
  .tech-mark { position: absolute; color: var(--text-white); font-weight: 700; letter-spacing: 2px; }
  .tech-mark.camera { left: 540px; top: 843px; font-size: 28px; }
  .tech-mark.sound { left: 531px; top: 905px; font-size: 20px; display: flex; align-items: center; gap: 8px; }
  .tech-mark.sound .box { width: 18px; height: 18px; background: var(--text-white); }

  .notes { position: absolute; left: 831px; top: 322px; width: 320px; color: var(--note-grey); font-weight: 300; }
  .notes h2 { font-weight: 300; font-size: 45px; line-height: 50px; margin-bottom: 28px; }
  .notes p { font-size: 21px; line-height: 28.5px; margin-bottom: 28px; }
</style>
</head>
<body>
  <section class="flyer">
    <div class="hero-photo" role="img" aria-label="Underwater shot of a couple embracing, silhouetted against a man's back in teal light"></div>
    <p class="hero-quote"><span class="qmark">“</span>The second film with Lukas Brenner after his award winning debut on screen in <span class="red">THE HOLLOW</span> side by side with the upcoming Mira Olsen Kade in the new flick of director Anton Reiss<span class="qmark">”</span></p>
    <h1 class="title">MARBLEFIN</h1>

    <div class="still-strip">
      <div class="still gym" role="img" aria-label="Film still: young man lifting weights in a gym"></div>
      <div class="still portrait" role="img" aria-label="Film still: young woman in a dim room"></div>
      <div class="still pregnant" role="img" aria-label="Film still: pregnant woman and man in an apartment"></div>
      <div class="still father" role="img" aria-label="Film still: man holding a newborn baby in a hallway"></div>
    </div>

    <div class="figure-shadow" role="img" aria-label="Dark silhouette of a man in a hooded sweater"></div>

    <span class="syn-open">“</span>
    <p class="synopsis"><span class="lead">A</span>fter the nuclear plant workers <b>DAVID</b> (24) and his pregnant girlfriend <b>JESSY</b> (22) are beaten in the main, David accesses steroids. But instead being able to preserve and to protect his girl and unborn baby, he is becoming a danger to them. Shortly before birth the amateur bodybuilder brutally beating up his love to the ground. She leaves him. Only after David has abducted his newborn daughter from the hospital, he notices his deadly dangerous trip. He brings back the child and asks Jessy to forgive him. <span class="qmark">”</span></p>

    <p class="specs">
      <span class="red">LOVE-DRAMA</span> | 110MIN | <span class="red">COLOR</span> | SWISS-GERMAN/GERMAN<br>
      KORVEN CAM | 1:1,85 | SONARA SOUND | BUDGET : <span class="red">EUR 1.6 MIL</span><br>
      RELEASE : <span class="red">FALL 2016</span>
    </p>

    <div class="contact">
      <h3>CONTACT</h3><br>
      Northwake Films<br>
      Tomas Vrelnik &nbsp;|&nbsp; Elias Fenner<br>
      Bergweg 12 &nbsp;| 8004 Lindau &nbsp;| &nbsp;Switzerland<br>
      Phone : +41 00 555 01 23<br>
      info@northwakefilms.example &nbsp;| &nbsp;www.northwake-films.example
    </div>

    <div class="tech-mark camera">KORVEN</div>
    <div class="tech-mark sound"><span class="box"></span>SONARA SOUND</div>
  </section>

  <aside class="notes">
    <h2>Sample Back</h2>
    <p>Again, the shade..</p>
    <p>I make it in a way that,,<br>the shade,, or his dark side or .. etc .. is affecting or ruining his entire life or something like that.</p>
    <p>Hope you can get the idea i want to present.</p>
    <p>Thanks, and hope you like them.</p>
  </aside>
</body>
</html>
```